Kelvo Auto - help to get me noticed

We not long ago tasked Pixel Harbour to design a logo for my business. I'm happy with the result so would like to have a business card designed as a follow up.

It's an Automotive service and repair business that offers the following -
- Servicing
- General repairs
- Brakes
- Detailing
- Integrity

Kelvo Automotive
Dallin Mereth
0471 926 317

Target Market(s)

Everyday people with the ability to reach out to corporate customers also.

Industry/Entity Type

Automotive

Contact Information for Business Card

Black card, logo, name and phone number on front. Other details on back of card.

```html
<!DOCTYPE html>
<html lang="en">
<head>
<meta charset="utf-8">
<title>Kelvo Automotive – Business Card</title>
<link rel="stylesheet" href="https://fonts.googleapis.com/css2?family=Teko:wght@600&family=Lato:wght@400&display=swap">
<style>
  :root {
    --backdrop: #9a9a9a;
    --card: #131315;
    --green-dark: #5fa045;
    --green-mid: #7db83c;
    --green-light: #b2cf35;
    --white: #ffffff;
  }
  * { box-sizing: border-box; margin: 0; padding: 0; }
  html, body {
    width: 1021px; height: 1200px; overflow: hidden;
    background: var(--backdrop);
  }
  .card {
    position: absolute;
    width: 753px; height: 429px;
    background: var(--card);
    overflow: hidden;
  }
  .card--front { left: 134px; top: 119px; }
  .card--back  { left: 131px; top: 651px; }

  .brand {
    position: absolute; left: 0; right: 0;
    display: flex; flex-direction: column; align-items: center;
    font-family: "Teko", sans-serif; font-weight: 600;
    color: var(--green-mid); text-transform: uppercase;
    line-height: 0.8;
  }
  .card--front .brand { top: 104px; }
  .card--front .brand__name { font-size: 112px; letter-spacing: 2px; }
  .card--front .brand__sub  { font-size: 42px; letter-spacing: 5px; margin-top: 6px; }
  .card--back .brand { top: 118px; }
  .card--back .brand__name { font-size: 140px; letter-spacing: 3px; }
  .card--back .brand__sub  { font-size: 52px; letter-spacing: 6px; margin-top: 8px; }

  .contact {
    position: absolute; top: 313px; left: 0; right: 0;
    display: flex; align-items: center; justify-content: center;
  }
  .contact__name {
    font-family: "Teko", sans-serif; font-weight: 600;
    font-size: 36px; line-height: 1; letter-spacing: 1.5px;
    color: var(--green-mid); text-transform: uppercase;
    padding-top: 6px;
  }
  .contact__divider {
    width: 1.5px; height: 46px; background: var(--green-mid);
    margin: 0 24px 0 20px;
  }
  .contact__phone {
    display: flex; align-items: center; gap: 7px;
    font-family: "Lato", sans-serif; font-size: 21px; color: var(--white);
  }
  .contact__icon { width: 19px; height: 19px; }

  .tagline {
    position: absolute; top: 334px; left: 0; right: 0;
    text-align: center;
    font-family: "Lato", sans-serif; font-size: 18px; color: var(--white);
  }
  .services {
    position: absolute; top: 372px; left: 0; right: 0; height: 33px;
    background: linear-gradient(90deg, var(--green-dark), var(--green-light));
    display: flex; align-items: center; justify-content: center; gap: 27px;
    list-style: none;
    font-family: "Lato", sans-serif; font-size: 18px; color: var(--white);
  }
  .services li::before { content: "•"; margin-right: 8px; font-size: 14px; vertical-align: 2px; }
</style>
</head>
<body>
  <section class="card card--front">
    <div class="brand">
      <span class="brand__name">Kelvo</span>
      <span class="brand__sub">Automotive</span>
    </div>
    <div class="contact">
      <span class="contact__name">Dallin Mereth</span>
      <span class="contact__divider"></span>
      <span class="contact__phone">
        <svg class="contact__icon" viewBox="0 0 20 20" aria-hidden="true">
          <circle cx="10" cy="10" r="10" fill="var(--green-mid)"/>
          <path d="M6.2 5.2c.5-.4 1.1-.3 1.4.2l1 1.6c.3.5.2 1-.2 1.4l-.6.5c.5 1.2 1.4 2.1 2.6 2.7l.5-.6c.4-.4 1-.5 1.4-.2l1.6 1c.5.3.6.9.2 1.4l-.7.9c-.4.5-1.1.7-1.7.5-3-1-5.2-3.2-6.2-6.2-.2-.6 0-1.3.5-1.7z" fill="var(--card)"/>
        </svg>
        0471 926 317
      </span>
    </div>
  </section>

  <section class="card card--back">
    <div class="brand">
      <span class="brand__name">Kelvo</span>
      <span class="brand__sub">Automotive</span>
    </div>
    <p class="tagline">It's an Automotive service and repair business that offers the following</p>
    <ul class="services">
      <li>Servicing</li>
      <li>General repairs</li>
      <li>Brakes</li>
      <li>Detailing</li>
      <li>Integrity</li>
    </ul>
  </section>
</body>
</html>
```